Responsive OnePage Design for recruitment company

BrightCrew is a modern company that sources interim people for its customers. Mostly developers, scrum master, project managers and designers. In this website we want to tell something about us, about how we work, our customers and we want our candidates be able to subscribe. The subscription form should be several fields (name, surname, email address, phone number and the possibility to upload your resume.We want it to fit into a existing wordpress plugin. We also want a listing of our job opportunities. The listing should be designed in a clear readable overview and if you click on the job you should get the details and be able to respond quickly by filling in you name, surname, email address, rate, phone number and upload your resume. We want this to be a standard configurable plugin. It should be easy to fill in the jobs in Wordpress by our administrator. We want a fresh, modern and cool design. It should be a responsive onepage design. If you click on a listed job you should stay on the same page. Our logo is added.

Target Market(s)

recruitment

Industry/Entity Type

Recruitment

Font styles to use
Sans Serif

Colors

Designer to choose colors to be used in the design.

Requirements
Must have
• Onepage design
• listing of job opportunities
• subscription forms
• be responsive

```html
<!DOCTYPE html>
<html lang="en">
<head>
<meta charset="utf-8">
<title>BrightCrew – Recruiting Expertise</title>
<link rel="stylesheet" href="https://fonts.googleapis.com/css2?family=Roboto:wght@300;400;500;700&display=swap">
<style>
  :root {
    --blue: #0a71b9;
    --blue-bright: #0d9ad8;
    --navy: #1a3b8f;
    --ink: #4a4a4a;
    --dark: #111111;
    --grey-bg: #efefef;
    --field-border: #c8c8c8;
    --field-fill: #c9c9c9;
    --table-head: #e6e6e6;
    --employer: #8a8a8a;
    --white: #ffffff;
  }
  * { box-sizing: border-box; margin: 0; padding: 0; }
  html, body { width: 1200px; height: 2281px; overflow: hidden; }
  body {
    position: relative;
    font-family: "Roboto", Arial, sans-serif;
    color: var(--ink);
    background: var(--white);
  }
  .abs { position: absolute; }

  /* Header */
  .brand { left: 30px; top: 26px; font-size: 29px; font-weight: 500; letter-spacing: 4px; color: var(--ink); }
  .social { left: 510px; top: 36px; display: flex; gap: 24px; }
  .social span { width: 10px; height: 10px; border-radius: 50%; background: var(--dark); display: block; }
  .top-nav { top: 33px; font-size: 13px; font-weight: 500; color: var(--dark); }
  .menu-btn { left: 1137px; top: 18px; width: 38px; height: 38px; border-radius: 50%; background: var(--blue); }
  .menu-btn i { position: absolute; left: 12px; width: 14px; height: 2px; background: var(--white); }

  /* Hero */
  .hero-photo { left: 585px; top: 60px; width: 615px; height: 579px; background: linear-gradient(160deg, #f4efe9 0%, #d9b48a 38%, #2a2a2a 75%, #111 100%); }
  .hero-kicker { right: 625px; top: 194px; font-size: 28px; font-weight: 300; color: var(--ink); white-space: nowrap; letter-spacing: -0.5px; }
  .hero-title { right: 625px; top: 232px; font-size: 84px; font-weight: 300; line-height: 74px; text-align: right; letter-spacing: -3px; color: var(--ink); white-space: nowrap; }
  .hero-title .accent { color: var(--blue); }
  .btn-enroll { left: 357px; top: 412px; width: 218px; height: 33px; border-radius: 3px; background: var(--blue); color: var(--white); font-size: 18px; font-weight: 500; text-align: center; line-height: 33px; }

  /* Quick search band */
  .search-band { left: 0; top: 639px; width: 1200px; height: 121px; background: var(--blue); }
  .search-title { left: 105px; top: 670px; font-size: 46px; font-weight: 300; color: var(--white); }
  .select { height: 33px; border-radius: 5px; background: var(--white); font-size: 16px; color: #888; padding: 7px 12px; }
  .select::after { content: "⌄"; position: absolute; right: 12px; top: 2px; font-size: 18px; color: #666; }
  .search-btn { left: 990px; top: 685px; width: 36px; height: 36px; border-radius: 50%; background: var(--dark); }

  /* Job listing */
  .section-heading { font-size: 46px; font-weight: 300; line-height: 49px; color: var(--ink); }
  .section-heading .accent { color: var(--blue); }
  .category-select { left: 103px; top: 932px; width: 226px; height: 33px; border: 1px solid var(--field-border); border-radius: 5px; background: var(--white); font-size: 16px; color: #888; padding: 6px 12px; }
  .category-select::after { content: "⌄"; position: absolute; right: 12px; top: 1px; font-size: 18px; color: #666; }
  .blurb { font-size: 8.5px; line-height: 13px; color: #555; width: 285px; }
  .job-table { left: 446px; top: 818px; width: 629px; height: 267px; background: #f7f7f7; box-shadow: 0 1px 3px rgba(0,0,0,.15); }
  .job-head { height: 38px; background: var(--table-head); font-size: 12px; color: var(--dark); position: relative; }
  .job-head span { position: absolute; top: 12px; }
  .job-row { position: absolute; left: 6px; width: 617px; height: 67px; background: var(--white); box-shadow: 0 1px 2px rgba(0,0,0,.12); }
  .job-meta { position: absolute; left: 20px; font-size: 8px; color: var(--dark); display: flex; align-items: center; gap: 6px; }
  .job-meta b { width: 10px; height: 10px; border-radius: 50%; background: var(--dark); display: block; }
  .job-title { position: absolute; left: 134px; top: 14px; font-size: 13px; color: var(--navy); }
  .job-sub { position: absolute; left: 134px; top: 36px; font-size: 8px; color: var(--dark); }
  .job-btn { position: absolute; left: 527px; top: 13px; width: 72px; height: 24px; background: var(--blue-bright); color: var(--white); font-size: 8px; font-weight: 700; text-align: center; line-height: 24px; }

  /* Subscription */
  .join-band { left: 0; top: 1145px; width: 1200px; height: 513px; background: var(--grey-bg); }
  .field { width: 226px; height: 33px; background: var(--white); border: 1px solid var(--field-border); border-radius: 5px; }
  .btn-submit-join { left: 786px; top: 1544px; width: 222px; height: 48px; background: var(--dark); color: var(--white); font-size: 26px; font-weight: 300; text-align: center; line-height: 48px; }

  /* Featured employers */
  .featured-box { left: 88px; top: 1746px; width: 279px; height: 122px; background: var(--blue); color: var(--white); font-size: 46px; font-weight: 300; line-height: 50px; padding: 12px 0 0 26px; }
  .employer { top: 1792px; font-size: 36px; font-weight: 700; color: var(--employer); text-align: center; line-height: 44px; }
  .scroll-track { left: 368px; top: 1881px; width: 744px; height: 11px; background: #dedede; }
  .scroll-thumb { left: 773px; top: 1881px; width: 73px; height: 11px; background: #a3a3a3; }

  /* Contact */
  .contact-band { left: 0; top: 1977px; width: 1200px; height: 263px; background: var(--grey-bg); }
  .contact-heading { left: 88px; top: 2025px; font-size: 46px; font-weight: 300; line-height: 49px; color: var(--ink); }
  .contact-heading .accent { color: var(--blue); }
  .contact-field { left: 485px; width: 345px; background: var(--field-fill); font-size: 11px; color: var(--dark); padding: 4px 6px; }
  .btn-submit { left: 762px; top: 2157px; width: 68px; height: 20px; background: var(--dark); color: var(--white); font-size: 11px; text-align: center; line-height: 20px; }
  .contact-label { left: 916px; font-size: 17px; font-weight: 700; letter-spacing: 2px; color: var(--dark); }
  .contact-value { left: 916px; font-size: 17px; letter-spacing: 1.5px; color: var(--dark); }

  /* Footer */
  .footer-dark { left: 0; top: 2240px; width: 389px; height: 41px; background: var(--dark); color: var(--white); font-size: 12px; line-height: 41px; padding-left: 58px; }
  .footer-blue { left: 389px; top: 2240px; width: 811px; height: 41px; background: var(--blue); }
</style>
</head>
<body>

<header>
  <div class="abs brand">BRIGHTCREW</div>
  <nav class="abs social" aria-label="Social links"><span></span><span></span><span></span><span></span><span></span><span></span></nav>
  <a class="abs top-nav" style="left:922px">Upload Resume</a>
  <a class="abs top-nav" style="left:1042px">Trending Jobs</a>
  <div class="abs menu-btn" aria-label="Menu"><i style="top:13px"></i><i style="top:18px"></i><i style="top:23px"></i></div>
</header>

<section class="hero">
  <div class="abs hero-photo" role="img" aria-label="Photo of a smiling recruiter in a dark blazer pointing toward the headline"></div>
  <p class="abs hero-kicker">Discover Your True Potential with our</p>
  <h1 class="abs hero-title">RECRUITING<br><span class="accent">EXPERTISE</span></h1>
  <a class="abs btn-enroll">ENROLL NOW</a>
</section>

<section class="abs search-band"></section>
<h2 class="abs search-title">Quick Job Search by</h2>
<div class="abs select" style="left:575px;top:687px;width:185px">Location</div>
<div class="abs select" style="left:786px;top:687px;width:187px">Industry</div>
<div class="abs search-btn" aria-label="Search">
  <svg width="36" height="36" viewBox="0 0 36 36"><circle cx="19" cy="16" r="6" fill="none" stroke="#fff" stroke-width="3"/><line x1="15" y1="20" x2="10" y2="26" stroke="#fff" stroke-width="3.5" stroke-linecap="round"/></svg>
</div>

<section class="jobs">
  <h2 class="abs section-heading" style="left:105px;top:820px">Popular<br><span class="accent">Job</span> Listing</h2>
  <div class="abs category-select">Selected Category</div>
  <p class="abs blurb" style="left:105px;top:981px">Our products are designed to instill life into extraordinary spaces, whatever their size. They're created for welcoming, hosting, entertaining. They're products of presence, made to be lived in and to endure the test of time.</p>

  <div class="abs job-table">
    <div class="job-head"><span style="left:20px">Pay</span><span style="left:110px">Job Title</span></div>
    <div class="job-row" style="top:44px">
      <div class="job-meta" style="top:16px"><b></b>New York</div>
      <div class="job-meta" style="top:34px"><b></b>up to $39.00</div>
      <div class="job-title">Business Analyst - New York</div>
      <div class="job-sub">Business Analyst - New York</div>
      <div class="job-btn">View details</div>
    </div>
    <div class="job-row" style="top:120px">
      <div class="job-meta" style="top:16px"><b></b>New York</div>
      <div class="job-meta" style="top:34px"><b></b>up to $39.00</div>
      <div class="job-title">Business Analyst - New York</div>
      <div class="job-sub">Business Analyst - New York</div>
      <div class="job-btn">View details</div>
    </div>
    <div class="job-row" style="top:196px">
      <div class="job-meta" style="top:16px"><b></b>New York</div>
      <div class="job-meta" style="top:34px"><b></b>up to $39.00</div>
      <div class="job-title">Business Analyst - New York</div>
      <div class="job-sub">Business Analyst - New York</div>
      <div class="job-btn">View details</div>
    </div>
  </div>
</section>

<section class="abs join-band"></section>
<h2 class="abs section-heading" style="left:105px;top:1200px">Be a Part of a<br><span class="accent">Global Staffing<br>Leader</span></h2>
<p class="abs blurb" style="left:105px;top:1372px">Our products are designed to instill life into extraordinary spaces, whatever their size. They're created for welcoming, hosting, entertaining. They're products of presence, made to be lived in and to endure the test of time.</p>
<div class="abs field" style="left:506px;top:1209px"></div><div class="abs field" style="left:785px;top:1209px"></div>
<div class="abs field" style="left:506px;top:1262px"></div><div class="abs field" style="left:785px;top:1262px"></div>
<div class="abs field" style="left:506px;top:1323px"></div><div class="abs field" style="left:785px;top:1323px"></div>
<div class="abs field" style="left:506px;top:1386px"></div><div class="abs field" style="left:785px;top:1386px"></div>
<div class="abs field" style="left:506px;top:1450px"></div><div class="abs field" style="left:785px;top:1450px"></div>
<a class="abs btn-submit-join">Enroll Now!</a>

<section class="employers">
  <h2 class="abs featured-box">Featured<br>Employers</h2>
  <div class="abs employer" style="left:414px;width:208px">Zentrilo</div>
  <div class="abs employer" style="left:689px;width:208px">Quorbeam</div>
  <div class="abs employer" style="left:950px;width:180px">Vaxmoro</div>
  <div class="abs scroll-track"></div>
  <div class="abs scroll-thumb"></div>
</section>

<section class="abs contact-band"></section>
<h2 class="abs contact-heading"><span class="accent">Get in Touch...</span><br>We will be glad<br>to assist you!</h2>
<div class="abs contact-field" style="top:2044px;height:22px">Name</div>
<div class="abs contact-field" style="top:2079px;height:23px">Email</div>
<div class="abs contact-field" style="top:2114px;height:32px">Query</div>
<a class="abs btn-submit">Submit</a>
<div class="abs contact-label" style="top:2044px">DIAL:</div>
<div class="abs contact-value" style="top:2068px">555.010.4821</div>
<div class="abs contact-label" style="top:2109px">Email:</div>
<div class="abs contact-value" style="top:2133px">hello@brightcrew.com</div>

<footer>
  <div class="abs footer-dark">©2019 BRIGHTCREW. ALL RIGHTS RESERVED.</div>
  <div class="abs footer-blue"></div>
</footer>

</body>
</html>
```